Circular Wedding Menu Design - Adobe Illustrator

I am looking for a design for circular wedding menus. these will be 7 inches.I'm providing a template from the printer, AI files of our wedding invitation, and the menu items.

The paper our invitations were printed on was a sandy beige color. please make the background for this the same color. It will be put ontop of a white plate with ivory tablecloth and cappucino covered napkins.

IMPORTANT - We aren't committed to a specific design so feel free to use whatever you like, but we definitely want the cow, fish, and carrot images from our rsvp to be used for the entrees in the menu.

IMPORTANT - must be in Adobe illustrator format

for inspiration:
http://cdn.velvorabridalnotes.example/wp-content/uploads/2012/10/tormane-styled-19.jpg

http://www.quorbelsearch.example/imgres?imgurl=http%3A%2F%2Fwww.dellivanestudio.example%2Fblog%2Fwp-content%2Fuploads%2F2013%2F07%2FPetal-Ledger-Round-Menu-Wedding-Place-Setting.jpg&imgrefurl=http%3A%2F%2Fwww.dellivanestudio.example%2Fblog%2Finspiration%2Fsimply-lovely-wedding-menu-place-settings%2F&h=815&w=600&tbnid=8kRqzp_4LUTWEN%3A&zoom=1&docid=72HJKs9PqMxaTN&ei=QwERtYu8LpMsoBF2xdDTRk&tbm=isch&ved=0DHtRNzhKNBk&iact=rc&uact=3&dur=526&page=1&start=0&ndsp=30

https://thumbs3.pixorvane.example/images?q=tbn:QWe7KpLmNvBxRtYu2Hs4DfGhJkZxCvBnMqWeRtYuIoPaSdFgHjK

https://thumbs3.pixorvane.example/images?q=tbn:ZxC8vBnMqW_e42RT_yUioPaSdFgHjKlZxCv66BnM7q_WERtyUiOp

https://thumbs2.pixorvane.example/images?q=tbn:LkJh5GfDsAp9OiUyTrEwQ-MNbV8cXzL3KjHgFdsaPoIuYtReW0Q

Industry/Entity Type

Wedding

```html
<!DOCTYPE html>
<html lang="en">
<head>
<meta charset="utf-8">
<title>Wedding Menu</title>
<link rel="stylesheet" href="https://fonts.googleapis.com/css2?family=Great+Vibes&family=Italianno&family=PT+Sans:wght@400;700&display=swap">
<style>
  :root {
    --page: #ffffff;
    --sand: #ece8dc;
    --sand-deep: #ddd7c6;
    --sand-light: #f5f2ea;
    --gold: #c09a3c;
    --ink: #1a1a1a;
    --icon: #000000;
  }
  html, body {
    margin: 0;
    padding: 0;
    width: 1200px;
    height: 1164px;
    overflow: hidden;
    background: var(--page);
  }
  .menu-card {
    position: relative;
    width: 1200px;
    height: 1164px;
    font-family: "PT Sans", "Arial Narrow", sans-serif;
    color: var(--ink);
  }
  .card-disc {
    position: absolute;
    inset: 0;
    border-radius: 50%;
    background:
      radial-gradient(ellipse at 50% 45%, var(--sand-light) 0%, var(--sand) 55%, var(--sand-deep) 100%);
  }
  .menu-title {
    position: absolute;
    left: 0;
    width: 1230px;
    top: 100px;
    margin: 0;
    text-align: center;
    font-family: "Great Vibes", cursive;
    font-weight: 400;
    font-size: 230px;
    line-height: 1;
    color: var(--ink);
    text-shadow: 5px 8px 6px rgba(0,0,0,0.35);
  }
  .section-title {
    position: absolute;
    margin: 0;
    font-family: "Italianno", cursive;
    font-weight: 400;
    font-size: 66px;
    line-height: 1;
    color: var(--gold);
  }
  .rules {
    position: absolute;
    inset: 0;
  }
  .dish {
    position: absolute;
    margin: 0;
    font-size: 23.5px;
    line-height: 33px;
    letter-spacing: 0.2px;
  }
  .dish strong { font-weight: 700; }
  .dish-icon {
    position: absolute;
    background: var(--icon);
  }
</style>
</head>
<body>
<main class="menu-card">
  <div class="card-disc" role="img" aria-label="Sandy beige round card with faint damask pattern and trailing grey leaf vines around the edge"></div>

  <svg class="rules" width="1200" height="1164" viewBox="0 0 1200 1164" aria-hidden="true">
    <g fill="none" stroke="var(--gold)" stroke-width="2">
      <line x1="119" y1="378" x2="1150" y2="378"/>
      <circle cx="112" cy="378" r="7" fill="var(--sand)"/>
      <path d="M119 378 C135 372 140 362 150 356"/>
      <line x1="8" y1="596" x2="540" y2="596"/>
      <circle cx="547" cy="596" r="7" fill="var(--sand)"/>
      <line x1="146" y1="960" x2="924" y2="960"/>
      <circle cx="931" cy="960" r="7" fill="var(--sand)"/>
    </g>
  </svg>

  <h1 class="menu-title">Menu</h1>

  <h2 class="section-title" style="left:146px; top:318px;">Salad</h2>
  <div class="dish-icon" style="left:176px; top:390px; width:46px; height:46px; border-radius:50%;" role="img" aria-label="Tomato silhouette icon"></div>
  <p class="dish" style="left:232px; top:393px; width:520px;"><strong>Grilled Watermelon &amp; Fig Salad:</strong> Gem Lettuces, Watermelon, Figs, Toasted Hazelnuts, Balsamic Reduction, Honey-Orange Dressing</p>

  <h2 class="section-title" style="left:388px; top:537px;">Entrée</h2>
  <div class="dish-icon" style="left:400px; top:611px; width:70px; height:58px; border-radius:8px;" role="img" aria-label="Cow silhouette icon"></div>
  <p class="dish" style="left:480px; top:614px; width:560px;">Roasted Filet Mignon, Wild Mushrooms, Garlic Mashed Potatoes, Asparagus with Red Wine Sauce</p>
  <div class="dish-icon" style="left:400px; top:695px; width:70px; height:52px; border-radius:50%;" role="img" aria-label="Fish silhouette icon"></div>
  <p class="dish" style="left:480px; top:696px; width:560px;">Porcini Crusted Halibut, Lemon-Herb Potatoes, Black Kale, Early Girl Tomatoes</p>
  <div class="dish-icon" style="left:406px; top:776px; width:52px; height:68px; border-radius:40% 40% 50% 10%;" role="img" aria-label="Carrot silhouette icon"></div>
  <p class="dish" style="left:480px; top:778px; width:560px;">Artichoke Agnolotti, Wild Mushrooms, Baby Arugula, Goat Cheese, White Wine Sauce, Micro Herbs</p>

  <h2 class="section-title" style="left:603px; top:892px;">Wedding Cake</h2>
  <div class="dish-icon" style="left:637px; top:985px; width:44px; height:50px; border-radius:14px 4px 2px 2px;" role="img" aria-label="Cake slice silhouette icon"></div>
  <p class="dish" style="left:694px; top:974px; width:400px;">Delicate Butter Pecan With Fresh Raspberry Mouse</p>
</main>
</body>
</html>
```